We Are Corvane Marketing Collateral

We Are Corvane has undergone a rebrand with new logo, website, and intranet design builds. The business is now looking to update its marketing collateral with the new logo design and colour palette. Deliverables include PowerPoint template, Report template, Letterhead, and Email signature. Refer attached design brief for more information. Also attached are the logo and brand document.
Target Market(s)
Executive & Board of SME impact organisations.
Industry/Entity Type
We serve small to medium organisations who are delivering impact, not-for-profits, social enterprises and purpose driven organisations.
Font styles to use
Other font styles liked:
- Roca Two Thin, Rubik Regular
Look and feel
Each slider illustrates characteristics of the customer's brand and the style your logo design should communicate.

```html
<!DOCTYPE html>
<html lang="en">
<head>
<meta charset="utf-8">
<title>Word Report Template – Corvane</title>
<link href="https://fonts.googleapis.com/css2?family=Fraunces:opsz,wght@9..144,300;9..144,400&family=Rubik:wght@400;500&display=swap" rel="stylesheet">
<style>
  :root{
    --stage:#d7f2ea;
    --forest:#1b4d45;
    --forest-text:#1e5a4f;
    --white:#ffffff;
    --ink:#2b2b2b;
    --sage:#9ccbbd;
    --bar-1:#7fa99a;
    --bar-2:#a8d4c5;
    --bar-3:#cfe6de;
    --grid:#e2e2e2;
    --table-head:#8fbfb0;
    --table-line:#7fa99a;
  }
  *{box-sizing:border-box;margin:0;padding:0}
  html,body{width:1200px;height:675px;overflow:hidden}
  body{background:var(--stage);position:relative;font-family:"Rubik",sans-serif;color:var(--ink)}
  .showcase-title{position:absolute;top:18px;left:0;width:1200px;text-align:center;
    font-family:"Fraunces",serif;font-weight:300;font-size:78px;color:var(--forest);letter-spacing:-0.5px;line-height:1.1}
  .page{position:absolute;top:172px;width:304px;height:429px;background:var(--white);
    box-shadow:0 2px 6px rgba(0,0,0,.18);overflow:hidden}
  .page--cover{left:78px;background:var(--forest);color:var(--white)}
  .page--two{left:448px}
  .page--three{left:818px}
  .cover-pattern{position:absolute;left:0;top:0;width:100%;height:180px;
    background:radial-gradient(circle at 30% 20%,#e0706a 0,transparent 45%),
               radial-gradient(circle at 75% 30%,#3aa0a8 0,transparent 45%),
               radial-gradient(circle at 15% 60%,#f09a4a 0,transparent 40%),
               linear-gradient(180deg,#4ea87a 0%,var(--forest) 100%);opacity:.75}
  .cover-title{position:absolute;left:35px;top:210px;font-family:"Fraunces",serif;font-weight:300;
    font-size:34px;line-height:1.22}
  .cover-subtitle{position:absolute;left:35px;top:318px;font-size:12px;font-weight:500}
  .brand{position:absolute;display:flex;align-items:center;gap:6px;font-family:"Rubik",sans-serif;font-weight:400;letter-spacing:1px}
  .brand-dot{border-radius:50%;background:currentColor;opacity:1}
  .cover-brand{left:0;width:100%;justify-content:center;top:392px;font-size:16px;color:var(--white)}
  .cover-brand .brand-dot{width:12px;height:12px}
  .page-brand{right:14px;top:14px;font-size:6px;color:var(--forest-text)}
  .page-brand .brand-dot{width:6px;height:6px}
  .page-heading{position:absolute;left:31px;top:33px;font-family:"Fraunces",serif;font-size:14px;color:var(--forest)}
  .page-subheading{position:absolute;left:31px;top:55px;font-size:9.5px;font-weight:500;color:var(--forest-text)}
  .copy{position:absolute;left:31px;width:244px;font-size:5.4px;line-height:1.5}
  .page--three .copy{left:31px;width:244px}
  .pull-quote{position:absolute;left:31px;top:142px;width:245px;height:50px;background:var(--sage);
    padding:11px 10px;font-family:"Fraunces",serif;font-weight:300;font-size:8px;line-height:1.45;color:var(--forest)}
  .chart{position:absolute;left:31px;top:251px;width:245px;height:87px;border:1px solid var(--grid)}
  .data-table{position:absolute;left:47px;top:80px;width:214px;border-collapse:collapse;font-size:5.4px}
  .data-table th{background:var(--table-head);color:var(--white);font-weight:500;padding:2.5px 4px;text-align:center}
  .data-table td{padding:2.5px 4px;text-align:center;border-bottom:1px solid var(--table-line)}
  .data-table td:first-child{text-align:left}
  .page-footer{position:absolute;left:31px;right:31px;bottom:12px;display:flex;justify-content:space-between;font-size:5.4px}
  .page-footer strong{color:var(--forest-text);font-weight:500}
  .showcase-brand{right:36px;top:618px;font-size:28px;color:var(--forest-text);letter-spacing:2px}
  .showcase-brand .brand-dot{width:26px;height:26px}
</style>
</head>
<body>
  <h1 class="showcase-title">Word Report Template</h1>

  <section class="page page--cover">
    <div class="cover-pattern" role="img" aria-label="Scattered coloured dot pattern in green, orange, pink, coral and teal"></div>
    <h2 class="cover-title">Annual Report<br>2022</h2>
    <p class="cover-subtitle">Editor or Subtitle Text</p>
    <div class="brand cover-brand"><span class="brand-dot"></span>CORVANE</div>
  </section>

  <section class="page page--two">
    <div class="brand page-brand"><span class="brand-dot"></span>Corvane</div>
    <h2 class="page-heading">Title Heading</h2>
    <p class="page-subheading">Subtitle Text Here</p>
    <p class="copy" style="top:82px">To get started right away, just tap any placeholder text (such as this) and start typing to replace it with your own.</p>
    <p class="copy" style="top:106px">Want to insert a picture from your files or add a shape, text box, or table? You got it! On the Insert tab of the ribbon, just tap the option you need.</p>
    <blockquote class="pull-quote">“Find even more easy-to-use tools on the Insert tab, such as to add a hyperlink or insert a comment”</blockquote>
    <p class="copy" style="top:203px">To get started right away, just tap any placeholder text (such as this) and start typing to replace it with your own.</p>
    <p class="copy" style="top:227px">Want to insert a picture from your files or add a shape, text box, or table? You got it! On the Insert tab of the ribbon, just tap the option you need.</p>
    <svg class="chart" viewBox="0 0 245 87" font-family="Rubik, sans-serif" font-size="5" fill="#555">
      <g stroke="#e2e2e2" stroke-width=".6">
        <line x1="18" y1="8" x2="238" y2="8"/><line x1="18" y1="17" x2="238" y2="17"/>
        <line x1="18" y1="26" x2="238" y2="26"/><line x1="18" y1="35" x2="238" y2="35"/>
        <line x1="18" y1="44" x2="238" y2="44"/><line x1="18" y1="53" x2="238" y2="53"/>
        <line x1="18" y1="62" x2="238" y2="62"/>
      </g>
      <g text-anchor="end">
        <text x="14" y="10">6</text><text x="14" y="19">5</text><text x="14" y="28">4</text>
        <text x="14" y="37">3</text><text x="14" y="46">2</text><text x="14" y="55">1</text><text x="14" y="64">0</text>
      </g>
      <g fill="var(--bar-1)">
        <rect x="30" y="23.3" width="9" height="38.7"/><rect x="86" y="39.5" width="9" height="22.5"/>
        <rect x="142" y="30.5" width="9" height="31.5"/><rect x="198" y="21.5" width="9" height="40.5"/>
      </g>
      <g fill="var(--bar-2)">
        <rect x="42" y="40.4" width="9" height="21.6"/><rect x="98" y="22.4" width="9" height="39.6"/>
        <rect x="154" y="45.8" width="9" height="16.2"/><rect x="210" y="36.8" width="9" height="25.2"/>
      </g>
      <g fill="var(--bar-3)">
        <rect x="54" y="44" width="9" height="18"/><rect x="110" y="44" width="9" height="18"/>
        <rect x="166" y="35" width="9" height="27"/><rect x="222" y="17" width="9" height="45"/>
      </g>
      <g text-anchor="middle">
        <text x="46" y="71">Q1</text><text x="102" y="71">Q2</text><text x="158" y="71">Q3</text><text x="214" y="71">Category 4</text>
      </g>
      <g font-size="4.6">
        <rect x="86" y="77" width="3" height="3" fill="var(--bar-1)"/><text x="91" y="80">Series 1</text>
        <rect x="111" y="77" width="3" height="3" fill="var(--bar-2)"/><text x="116" y="80">Series 2</text>
        <rect x="136" y="77" width="3" height="3" fill="var(--bar-3)"/><text x="141" y="80">Series 3</text>
      </g>
    </svg>
    <p class="copy" style="top:347px">To get started right away, just tap any placeholder text (such as this) and start typing to replace it with your own.</p>
    <p class="copy" style="top:371px">Want to insert a picture from your files or add a shape, text box, or table? You got it! On the Insert tab of the ribbon, just tap the option you need.</p>
    <footer class="page-footer"><span><strong>We Are Corvane</strong> | Annual Report 2022</span><span>2</span></footer>
  </section>

  <section class="page page--three">
    <div class="brand page-brand"><span class="brand-dot"></span>Corvane</div>
    <p class="copy" style="top:8px">To get started right away, just tap any placeholder text (such as this) and start typing to replace it with your own.</p>
    <p class="copy" style="top:32px">Want to insert a picture from your files or add a shape, text box, or table? You got it! On the Insert tab of the ribbon, just tap the option you need.</p>
    <table class="data-table">
      <thead><tr><th></th><th>CATEGORY 1</th><th>CATEGORY 2</th><th>CATEGORY 3</th><th>CATEGORY 4</th></tr></thead>
      <tbody>
        <tr><td>Q1</td><td>4.5</td><td>2.3</td><td>1.7</td><td>5.0</td></tr>
        <tr><td>Q2</td><td>3.2</td><td>5.1</td><td>4.4</td><td>3.0</td></tr>
        <tr><td>Q3</td><td>2.1</td><td>1.7</td><td>2.5</td><td>2.8</td></tr>
        <tr><td>Q4</td><td>4.5</td><td>2.2</td><td>1.7</td><td>7.0</td></tr>
      </tbody>
    </table>
    <p class="copy" style="top:150px">To get started right away, just tap any placeholder text (such as this) and start typing to replace it with your own.</p>
    <p class="copy" style="top:174px">Want to insert a picture from your files or add a shape, text box, or table? You got it! On the Insert tab of the ribbon, just tap the option you need.</p>
    <footer class="page-footer"><span><strong>We Are Corvane</strong> | Annual Report 2022</span><span>3</span></footer>
  </section>

  <div class="brand showcase-brand"><span class="brand-dot"></span>CORVANE</div>
</body>
</html>
```